Become a Mentor - For Musicians, Artists, Producers and Teachers

Here is the full creative brief:

https://files.plenwick.com/sheets/d/4kTqpLm8Wz_2RNa7Hc3Xv91Jd0Gb5YeUsQ6fNo8rTpxa/view?mode=shared

Here is the background image file: https://www.trovecrate.com/sh/83jbwtrmq5dkx2u/BBHn4k7QTf2ZpLeXX-wr9MUHe?dl=0

LOGO:
https://www.trovecrate.com/sh/k472rufmpdo9b6w/BBKLe3RtHY5J-sFQnLZw7Ggma?dl=0

```html
<!DOCTYPE html>
<html lang="en">
<head>
<meta charset="utf-8">
<title>Become a Mentor – Meridian School of Music</title>
<link rel="stylesheet" href="https://fonts.googleapis.com/css2?family=Open+Sans:wght@400;600;700&family=Raleway:wght@300;400&family=Courgette&display=swap">
<style>
  :root {
    --navy-deep: #0b0b17;
    --navy: #161729;
    --sky: #2ea3dd;
    --sky-pale: #cfe9f8;
    --ice: #e6f3fb;
    --ribbon: #bfe2f6;
    --ribbon-text: #2b8fcc;
    --white: #ffffff;
    --ink: #111111;
    --violet: #3a2f6b;
    --wall: #77736d;
    --wall-dark: #3b3834;
    --shirt: #d9d2c6;
    --skin: #5a3a28;
    --jacket: #26211d;
    --desk: #4a4a3a;
    --shadow: #151418;
  }
  html, body { margin: 0; padding: 0; overflow: hidden; background: #d9d9d9; }
  .flyer {
    position: relative;
    width: 946px;
    height: 1200px;
    overflow: hidden;
    background: radial-gradient(ellipse at 40% 85%, var(--navy) 0%, var(--navy-deep) 75%);
    font-family: "Raleway", sans-serif;
    color: var(--white);
  }
  .hero-photo { position: absolute; left: 0; top: 0; width: 946px; height: 810px; }
  .enrol-tag {
    position: absolute; left: 45px; top: 0; width: 244px; height: 139px;
    display: flex; align-items: center; justify-content: center;
    font-family: "Open Sans", sans-serif; font-weight: 700;
    font-size: 40px; line-height: 1.2; text-align: center; color: var(--white);
  }
  .enrol-tag svg { position: absolute; inset: 0; z-index: 0; }
  .enrol-tag span { position: relative; z-index: 1; margin-top: -8px; }
  .apply-badge { position: absolute; left: 682px; top: 622px; width: 200px; height: 200px; }
  .kicker {
    position: absolute; left: 45px; top: 773px;
    font-weight: 300; font-size: 30px; letter-spacing: 0.4px; color: var(--ice);
  }
  .headline {
    position: absolute; left: 52px; top: 808px; margin: 0;
    font-family: "Courgette", cursive; font-weight: 400;
    font-size: 64px; line-height: 1.2; color: var(--sky-pale);
  }
  .subline {
    position: absolute; left: 53px; top: 902px; margin: 0;
    font-family: "Open Sans", sans-serif; font-weight: 400;
    font-size: 24px; line-height: 30px; letter-spacing: 1.3px;
    color: var(--sky); text-transform: uppercase; white-space: nowrap;
  }
  .brand { position: absolute; left: 66px; top: 1040px; width: 380px; }
  .brand-name {
    display: flex; align-items: center; gap: 14px;
    font-family: "Open Sans", sans-serif; font-weight: 700;
    font-size: 31px; line-height: 1.05; color: var(--white); letter-spacing: 1px;
  }
  .brand-dot { width: 56px; height: 56px; border-radius: 50%; background: var(--sky); flex: none; }
  .brand-tagline {
    margin-top: 30px; font-family: "Raleway", sans-serif; font-size: 13px; color: var(--ice);
  }
  .call-cue {
    position: absolute; right: 56px; top: 1002px;
    font-family: "Courgette", cursive; font-size: 31px; color: var(--ice);
  }
  .contact-panel { position: absolute; left: 456px; top: 1055px; width: 490px; height: 94px; }
  .contact-list {
    position: absolute; right: 58px; top: 1061px; margin: 0; padding: 0; list-style: none;
    font-family: "Open Sans", sans-serif; font-weight: 700; font-size: 16.5px; color: var(--ink);
  }
  .contact-list li { display: flex; justify-content: flex-end; align-items: center; gap: 8px; height: 23.5px; }
  .contact-icon { width: 19px; height: 19px; flex: none; }
</style>
</head>
<body>
<main class="flyer">

  <svg class="hero-photo" viewBox="0 0 946 810" role="img" aria-label="Photo: two musicians talking beside a mixing desk and studio monitor in a recording studio">
    <defs>
      <linearGradient id="wallTone" x1="0" y1="0" x2="1" y2="1">
        <stop offset="0" stop-color="var(--wall-dark)"/>
        <stop offset="0.35" stop-color="var(--wall)"/>
        <stop offset="0.75" stop-color="var(--wall-dark)"/>
        <stop offset="1" stop-color="var(--shadow)"/>
      </linearGradient>
      <radialGradient id="shirtGlow" cx="0.15" cy="0.55" r="0.32">
        <stop offset="0" stop-color="var(--shirt)" stop-opacity="0.9"/>
        <stop offset="1" stop-color="var(--shirt)" stop-opacity="0"/>
      </radialGradient>
      <radialGradient id="jacketShade" cx="0.83" cy="0.55" r="0.35">
        <stop offset="0" stop-color="var(--jacket)" stop-opacity="0.95"/>
        <stop offset="1" stop-color="var(--jacket)" stop-opacity="0"/>
      </radialGradient>
      <radialGradient id="skinWarm" cx="0.75" cy="0.33" r="0.14">
        <stop offset="0" stop-color="var(--skin)" stop-opacity="0.7"/>
        <stop offset="1" stop-color="var(--skin)" stop-opacity="0"/>
      </radialGradient>
      <radialGradient id="deskTone" cx="0.48" cy="0.68" r="0.3">
        <stop offset="0" stop-color="var(--desk)" stop-opacity="0.8"/>
        <stop offset="1" stop-color="var(--desk)" stop-opacity="0"/>
      </radialGradient>
      <linearGradient id="topShade" x1="0" y1="0" x2="0" y2="1">
        <stop offset="0" stop-color="var(--shadow)" stop-opacity="0.7"/>
        <stop offset="0.25" stop-color="var(--shadow)" stop-opacity="0"/>
      </linearGradient>
      <clipPath id="photoClip"><polygon points="0,0 946,0 946,800 0,612"/></clipPath>
    </defs>
    <g clip-path="url(#photoClip)">
      <rect width="946" height="810" fill="url(#wallTone)"/>
      <rect width="946" height="810" fill="url(#deskTone)"/>
      <rect width="946" height="810" fill="url(#shirtGlow)"/>
      <rect width="946" height="810" fill="url(#jacketShade)"/>
      <rect width="946" height="810" fill="url(#skinWarm)"/>
      <rect width="946" height="810" fill="url(#topShade)"/>
    </g>
    <path d="M0 614 Q 320 648 946 748" stroke="var(--shadow)" stroke-width="12" fill="none"/>
    <path d="M10 606 Q 320 630 700 672" stroke="#3a3a44" stroke-width="2" fill="none"/>
  </svg>

  <div class="enrol-tag">
    <svg viewBox="0 0 244 139" aria-hidden="true">
      <path d="M0 0 H244 V128 L232 132 L214 126 L190 134 L160 128 L130 136 L96 128 L64 135 L34 127 L12 134 L0 130 Z" fill="var(--sky)"/>
    </svg>
    <span>ENROL<br>TODAY</span>
  </div>

  <svg class="apply-badge" viewBox="0 0 200 200" aria-label="Apply now">
    <circle cx="100" cy="100" r="86" fill="none" stroke="var(--ice)" stroke-width="4"/>
    <g fill="var(--ice)">
      <circle cx="82" cy="40" r="4"/><circle cx="100" cy="42" r="4"/><circle cx="118" cy="44" r="4"/>
      <circle cx="82" cy="162" r="4"/><circle cx="100" cy="164" r="4"/><circle cx="118" cy="166" r="4"/>
    </g>
    <g transform="rotate(11 100 100)">
      <rect x="-4" y="76" width="208" height="50" fill="var(--ribbon)"/>
      <text x="100" y="111" text-anchor="middle" font-family="Open Sans, sans-serif" font-weight="700" font-size="28" fill="var(--ribbon-text)">APPLY NOW</text>
    </g>
  </svg>

  <div class="kicker">Start Your Career</div>
  <h1 class="headline">Become a Mentor</h1>
  <p class="subline">Turn your skills and passion for music into a career<br>designed for musicians, artists, producers &amp; teachers</p>

  <div class="brand">
    <div class="brand-name"><span class="brand-dot"></span><span>MERIDIAN<br>SCHOOL OF MUSIC</span></div>
    <div class="brand-tagline">...evolving a culture of Inspiration &amp; Creativity.</div>
  </div>

  <div class="call-cue">call us now</div>

  <svg class="contact-panel" viewBox="0 0 490 94" aria-hidden="true">
    <path d="M28 4 L120 1 L300 3 L490 0 L490 94 L300 91 L120 93 L40 90 L20 84 L42 78 L8 70 L30 62 L2 54 L26 46 L12 36 L34 28 L16 16 Z" fill="var(--white)"/>
  </svg>

  <ul class="contact-list">
    <li>0400 555 182 (03) 9000 4417
      <svg class="contact-icon" viewBox="0 0 20 20"><rect width="20" height="20" rx="3" fill="var(--violet)"/><path d="M6 4 L8.5 4 L9.5 7 L8 8.3 Q9.5 11.5 11.7 12 L13 10.5 L16 11.5 L16 14 Q15 16 12.5 15.5 Q5 13 4.5 6.5 Q4.5 4.5 6 4 Z" fill="var(--white)"/></svg>
    </li>
    <li>dana@meridianschoolofmusic.com.au
      <svg class="contact-icon" viewBox="0 0 20 20"><rect width="20" height="20" rx="3" fill="var(--violet)"/><rect x="4" y="6" width="12" height="8.5" fill="none" stroke="var(--white)" stroke-width="1.4"/><path d="M4 6 L10 11 L16 6" fill="none" stroke="var(--white)" stroke-width="1.4"/></svg>
    </li>
    <li>meridianschoolofmusic.com.au
      <svg class="contact-icon" viewBox="0 0 20 20"><rect width="20" height="20" rx="3" fill="var(--violet)"/><g fill="none" stroke="var(--white)" stroke-width="1.3"><circle cx="10" cy="10" r="5.5"/><ellipse cx="10" cy="10" rx="2.4" ry="5.5"/><path d="M4.5 10 H15.5"/></g></svg>
    </li>
  </ul>

</main>
</body>
</html>
```